Wellness Thai Massage Geschäft benötigt eine Preis/Info Broschüre

Ein kleines Thai Massage Geschäft in Bayern: Kolavan Thaimassage
Benötigt eine kleine Preisliste, sowie eine kurze Beschreibung vom Unternehmen. Angeboten werden traditionelle Thaimassagen. Der Farbstil soll dem Logo (Anhang) angepasst sein. Alle Bilder außer die Bilder von der Geschäftsführerin sind optional zur Verwendung verfügbar. Mehr Info wie Preise, etc. sind verfügbar auf der Website https://www.kolavanthaimassage.example/

```html
<!DOCTYPE html>
<html lang="de">
<head>
<meta charset="utf-8">
<title>Kolavan Thaimassage – Preisliste</title>
<link href="https://fonts.googleapis.com/css2?family=Hind:wght@400;600;700&family=Marcellus+SC&display=swap" rel="stylesheet">
<style>
  :root{
    --bg:#e8e5e1;
    --paper:#ffffff;
    --wine:#8b1a26;
    --cream:#f6ebc3;
    --ink:#3a2a2a;
    --pink:#d98fb4;
  }
  *{box-sizing:border-box;margin:0;padding:0}
  html,body{width:1200px;height:800px;overflow:hidden;background:var(--bg)}
  body{font-family:"Hind",sans-serif;color:var(--ink)}
  .flyer{position:absolute;left:320px;top:10px;width:560px;height:780px;background:var(--paper);box-shadow:0 2px 8px rgba(0,0,0,.15)}
  .block,.photo{position:absolute}
  .orchid{left:16px;top:16px;width:64px;height:74px;background:radial-gradient(circle at 50% 50%,var(--pink) 0 30%,var(--cream) 60%)}
  .title-band{left:80px;top:16px;width:208px;height:74px;background:var(--wine);color:var(--cream);font-family:"Marcellus SC",serif;font-size:21px;line-height:24px;letter-spacing:2px;padding:14px 0 0 16px}
  .title-band span{display:block}
  .title-band span+span{padding-left:10px}
  .photo-buddha{left:296px;top:16px;width:248px;height:200px;background:linear-gradient(135deg,#d9d2c4 0%,#6b4a3a 45%,#b8485a 70%,#e9c9a8 100%)}
  .photo-session{left:16px;top:96px;width:272px;height:232px;background:linear-gradient(160deg,#f0d99a 0%,#c9a472 35%,#8a2230 60%,#e7e2dc 100%)}
  .photo-stretch{left:296px;top:222px;width:248px;height:418px;background:linear-gradient(170deg,#f4f0e8 0%,#a52a35 30%,#8c3d3a 55%,#d9a57a 75%,#e9e6ef 100%)}
  .welcome{left:16px;top:334px;width:272px;height:56px;background:var(--wine);color:#fff;font-weight:700;font-size:14px;line-height:17px;padding:11px 10px}
  .welcome span{display:block;white-space:nowrap}
  .services{left:16px;top:398px;width:272px;height:320px;padding:0 6px 0 10px;display:flex;flex-direction:column;justify-content:space-between}
  .service h3{color:var(--wine);font-size:11.5px;line-height:13px;font-weight:700}
  .service p{font-size:6.5px;line-height:7.9px;text-align:justify}
  .prices{display:flex;gap:6px;margin-top:2px}
  .price{display:flex;align-items:center;background:var(--wine);color:#fff;font-size:7.5px;font-weight:600;height:12px;padding:0 2px 0 5px;white-space:nowrap}
  .price b{background:var(--cream);color:var(--wine);margin-left:4px;padding:0 4px;height:10px;line-height:11px;font-weight:700}
  .contact-bar{left:16px;top:726px;width:272px;height:38px;background:var(--wine);color:#fff;display:flex;align-items:center;justify-content:space-between;gap:8px;padding:0 8px;font-size:9.5px;font-weight:600}
  .web-bar{left:296px;top:646px;width:248px;height:30px;background:var(--wine);color:#fff;display:flex;align-items:center;gap:6px;padding:0 10px;font-size:10.5px;font-weight:600}
  .item{display:flex;align-items:center;gap:4px;white-space:nowrap}
  .icon{width:14px;height:14px;flex:none}
</style>
</head>
<body>
<main class="flyer">
  <div class="photo orchid" role="img" aria-label="Pinke Orchideenblüte auf cremefarbenem Grund"></div>
  <header class="block title-band"><span>Kolavan</span><span>Thaimassage</span></header>
  <div class="photo photo-buddha" role="img" aria-label="Buddha-Statue mit Orchideenblüten in einer Schale"></div>
  <div class="photo photo-session" role="img" aria-label="Masseurin bei einer traditionellen Thai-Massage im Behandlungsraum"></div>
  <div class="photo photo-stretch" role="img" aria-label="Masseurin dehnt den Arm einer Kundin auf der Massagematte"></div>

  <h1 class="block welcome"><span>Willkommen auf der Homepage von</span><span>Kolavan Thaimassage.</span></h1>

  <section class="block services">
    <article class="service">
      <h3>Traditionelle Thai-Sport Massage</h3>
      <p>Mit der traditionellen Thai-Massage werden durch Akupressur, Dehnung und Energielinien-Massage Energieblockaden gelöst. Es wird an 10 Energiepunkten und Linien massiert, die für den Einklang von Körper und Geist wichtig sind. Somit wird eine innere Balance und der Fluss der Lebensenergie erreicht.</p>
      <div class="prices"><span class="price">60 Minuten =<b>54 Euro</b></span><span class="price">90 Minuten =<b>76 Euro</b></span></div>
    </article>
    <article class="service">
      <h3>Aromaöl Massage</h3>
      <p>Die Aromaöl Massage ist eine Behandlungsform zur Regeneration und Harmonisierung des gesamten Körpers. Dabei wird das Basisöl mit ätherischen Ölen angereichert. Die Aromatherapie kann anregend oder entspannend abgestimmt werden.</p>
      <div class="prices"><span class="price">60 Minuten =<b>51 Euro</b></span><span class="price">90 Minuten =<b>72 Euro</b></span></div>
    </article>
    <article class="service">
      <h3>Hot Stone Massage</h3>
      <p>Bei der Hot Stone Massage werden angewärmte Vulkansteine entlang der Energielinien angebracht. Durch die abgegebene gespeicherte Wärme wird der Energiefluss und die Blutzirkulation gesteigert. Es kommt im ganzen Körper zu einer Tiefenentspannung.</p>
      <div class="prices"><span class="price">90 Minuten =<b>83 Euro</b></span></div>
    </article>
    <article class="service">
      <h3>Fussreflexzonen Massage</h3>
      <p>Eine Massage für den Wohl für den strapaziertesten Körperteil, den Füssen, setzt neue Kräfte frei und verleiht Vitalität.</p>
      <div class="prices"><span class="price">30 Minuten =<b>35 Euro</b></span><span class="price">60 Minuten =<b>62 Euro</b></span></div>
    </article>
    <article class="service">
      <h3>Rücken-Thai Massage</h3>
      <p>Bei dieser Massagetechnik wird größtenteils der Rücken sowie auch Nacken, Hinterkopf, Schulter und Finger involviert. Diese Massage eignet sich besonders falls eines dieser Bereiche verspannt oder Schmerzen verursacht.</p>
      <div class="prices"><span class="price">30 Minuten =<b>35 Euro</b></span><span class="price">60 Minuten =<b>72 Euro</b></span></div>
    </article>
  </section>

  <footer class="block contact-bar">
    <span class="item">
      <svg class="icon" viewBox="0 0 14 14"><circle cx="7" cy="7" r="6.5" fill="#fff"/><path d="M4.6 3.8l1.3-.3.8 1.8-.9.7a5 5 0 0 0 2.2 2.2l.7-.9 1.8.8-.3 1.3c-3 .3-5.9-2.6-5.6-5.6z" fill="#8b1a26"/></svg>
      01705550123
    </span>
    <span class="item">
      <svg class="icon" viewBox="0 0 14 14"><circle cx="7" cy="7" r="6.5" fill="#fff"/><rect x="3.5" y="4.5" width="7" height="5" fill="none" stroke="#8b1a26" stroke-width="1"/><path d="M3.5 4.5L7 7.3l3.5-2.8" fill="none" stroke="#8b1a26" stroke-width="1"/></svg>
      kolavan.thaimassage@example.com
    </span>
  </footer>

  <div class="block web-bar">
    <svg class="icon" viewBox="0 0 14 14"><circle cx="7" cy="7" r="6.5" fill="#fff"/><circle cx="7" cy="7" r="4" fill="none" stroke="#8b1a26" stroke-width="1"/><ellipse cx="7" cy="7" rx="1.7" ry="4" fill="none" stroke="#8b1a26" stroke-width=".8"/><path d="M3 7h8" stroke="#8b1a26" stroke-width=".8"/></svg>
    www.kolavanthaimassage.example
  </div>
</main>
</body>
</html>
```